Business Stationary
Velquor Group - Consulting Firm
Professional
Dale Whitford
CEO/President
482 W. Larkspur Ave
Suite 1475
Chicago, IL 60618
dwhitford@thevelquorgroup.example
www.thevelquorgroup.example
I am putting two versions of our logo for your use.

```html
<!DOCTYPE html>
<html lang="en">
<head>
<meta charset="utf-8">
<title>The Velquor Group — Business Cards</title>
<link rel="stylesheet" href="https://fonts.googleapis.com/css2?family=Cinzel:wght@400;600&family=Lato:wght@400&display=swap">
<style>
  :root {
    --page: #e9eaec;
    --card-white: #ffffff;
    --brand-red: #e0262c;
    --brand-red-deep: #b8161c;
    --ink: #1d1d1f;
    --muted: #555a60;
    --shadow: rgba(0, 0, 0, 0.18);
  }
  * { box-sizing: border-box; margin: 0; padding: 0; }
  html, body { width: 1200px; height: 980px; overflow: hidden; }
  body {
    background: var(--page);
    position: relative;
    font-family: "Lato", sans-serif;
  }
  .card {
    position: absolute;
    width: 560px;
    height: 320px;
    border-radius: 20px;
    overflow: hidden;
    box-shadow: 0 14px 30px var(--shadow);
  }

  /* Back card */
  .card-back {
    left: 560px;
    top: 130px;
    background: radial-gradient(ellipse at 50% 45%, var(--brand-red) 0%, var(--brand-red-deep) 100%);
    display: flex;
    align-items: center;
    justify-content: center;
  }
  .wordmark {
    display: flex;
    align-items: center;
    gap: 14px;
    font-family: "Cinzel", serif;
    font-weight: 400;
    letter-spacing: 0.04em;
  }
  .wordmark-dot {
    width: 16px;
    height: 16px;
    border-radius: 50%;
  }
  .card-back .wordmark { color: #ffffff; font-size: 30px; }
  .card-back .wordmark-dot { background: #ffffff; }

  /* Front card */
  .card-front {
    left: 120px;
    top: 500px;
    background: var(--card-white);
  }
  .front-art {
    position: absolute;
    inset: 0;
    width: 100%;
    height: 100%;
  }
  .card-front .wordmark {
    position: absolute;
    left: 32px;
    top: 30px;
    color: var(--brand-red);
    font-size: 22px;
  }
  .card-front .wordmark-dot { background: var(--brand-red); width: 12px; height: 12px; }
  .contact-list {
    position: absolute;
    left: 34px;
    top: 84px;
    list-style: none;
    font-size: 11px;
    color: var(--muted);
    letter-spacing: 0.03em;
    line-height: 17px;
  }
  .contact-list li { display: flex; align-items: center; gap: 8px; }
  .contact-icon { width: 11px; height: 11px; flex: none; }
  .contact-list li.indent { padding-left: 19px; }
  .signature {
    position: absolute;
    right: 30px;
    bottom: 22px;
    text-align: right;
    color: #ffffff;
    font-family: "Cinzel", serif;
  }
  .signature-name { font-size: 15px; font-weight: 600; letter-spacing: 0.05em; }
  .signature-title { font-size: 10px; letter-spacing: 0.12em; margin-top: 2px; }
</style>
</head>
<body>

  <section class="card card-back" aria-label="Business card, back">
    <div class="wordmark"><span class="wordmark-dot"></span><span>The Velquor Group</span></div>
  </section>

  <section class="card card-front" aria-label="Business card, front">
    <svg class="front-art" viewBox="0 0 560 320" preserveAspectRatio="none" aria-hidden="true">
      <path d="M0 250 C 150 300, 330 250, 560 150 L560 320 L0 320 Z" fill="var(--brand-red)"/>
      <path d="M0 232 C 150 282, 330 236, 560 132 L560 146 C 330 246, 150 292, 0 246 Z" fill="var(--ink)"/>
      <path d="M0 222 C 160 262, 330 222, 560 120" fill="none" stroke="var(--brand-red)" stroke-width="2"/>
    </svg>

    <div class="wordmark"><span class="wordmark-dot"></span><span>The Velquor Group</span></div>

    <ul class="contact-list">
      <li>
        <svg class="contact-icon" viewBox="0 0 12 12"><circle cx="6" cy="6" r="6" fill="var(--brand-red)"/><path d="M6 2.5a2 2 0 0 1 2 2c0 1.5-2 4-2 4s-2-2.5-2-4a2 2 0 0 1 2-2z" fill="#fff"/></svg>
        482 W. Larkspur Ave, Suite 1475
      </li>
      <li class="indent">Chicago, IL 60618</li>
      <li>
        <svg class="contact-icon" viewBox="0 0 12 12"><circle cx="6" cy="6" r="6" fill="var(--brand-red)"/><rect x="4.3" y="2.6" width="3.4" height="6.8" rx="0.8" fill="#fff"/></svg>
        T: 312.555.0148
      </li>
      <li>
        <svg class="contact-icon" viewBox="0 0 12 12"><circle cx="6" cy="6" r="6" fill="var(--brand-red)"/><rect x="3" y="4.5" width="6" height="3.5" fill="#fff"/><rect x="4" y="2.8" width="4" height="1.4" fill="#fff"/></svg>
        F: 708.555.0192
      </li>
      <li>
        <svg class="contact-icon" viewBox="0 0 12 12"><circle cx="6" cy="6" r="6" fill="var(--brand-red)"/><rect x="3" y="3.8" width="6" height="4.4" fill="#fff"/><path d="M3 3.8 L6 6.3 L9 3.8" fill="none" stroke="var(--brand-red)" stroke-width="0.8"/></svg>
        dwhitford@thevelquorgroup.example
      </li>
      <li>
        <svg class="contact-icon" viewBox="0 0 12 12"><circle cx="6" cy="6" r="6" fill="var(--brand-red)"/><circle cx="6" cy="6" r="3" fill="none" stroke="#fff" stroke-width="0.9"/><path d="M3 6h6M6 3v6" stroke="#fff" stroke-width="0.7"/></svg>
        www.thevelquorgroup.example
      </li>
    </ul>

    <div class="signature">
      <div class="signature-name">Dale Whitford</div>
      <div class="signature-title">CEO/PRESIDENT</div>
    </div>
  </section>

</body>
</html>
```